Brellin Trade Partners - we are Asian sourcing agents

We are sourcing agents based in the USA and we act as sourcing agents for clients in throughout the world. We focus primarily on custom sewn goods. So basically companies who do not have the in-house expertise to do it themselves, come to us and have us find suitable factories in Asia to do the production. We are middlemen. We find the factories...quote the project...manage the quality control and then deliver the goods directly to our customer's door. We pride ourselves in making the communication very easy and precise.

Current page is www.brellintrade.example

I am not happy w/ the overall look. The spacing...the photos, the fonts...the design elements...the pictures. I want a cool, crisp design that conveys professionalism and clearly depicts/explains what we do.

Requirements
Must have
• use my logo....I like it...it was designed by someone on this website.
Nice to have
• a video/animation of the entire process would be wonderful. Showing initial contact with our office in the USA...then to my correspondence with my offices in Taiwan and in Hong Kong...and then back and fort w/ the customer.....and then between my people in Hong Kong/Taiwan with the local factories......and then a quote is generated and sent to my client......to samples being made and sent for approval.....to a PO being generated......to final samples being sent.....to the order being shipped and delivered to the clients warehouse. I was thinking of an animation showing arrows and text showing the back and forth communication and explaining how the process flows.

```html
<!DOCTYPE html>
<html lang="en">
<head>
<meta charset="utf-8">
<title>Brellin Trade Partners</title>
<link rel="stylesheet" href="https://fonts.googleapis.com/css2?family=Open+Sans:wdth,wght@75..100,300..800&display=swap">
<style>
  :root {
    --green: #76921a;
    --green-dark: #5f7813;
    --ink: #1c1c1c;
    --text: #444444;
    --panel-light: #efefef;
    --content-bg: #f7f7f7;
    --footer-bg: #f2f2f2;
    --dark-1: #1b1b1b;
    --dark-2: #222222;
    --white: #ffffff;
    --bg-blue-deep: #020a3a;
    --bg-blue: #0b3fd6;
  }
  * { box-sizing: border-box; margin: 0; padding: 0; }
  html, body { width: 1200px; height: 1166px; overflow: hidden; }
  body {
    position: relative;
    font-family: "Open Sans", Arial, sans-serif;
    color: var(--text);
  }
  .backdrop {
    position: absolute; inset: 0;
    background:
      radial-gradient(ellipse at 50% 45%, rgba(60,120,255,0.55) 0%, transparent 55%),
      radial-gradient(ellipse at 5% 80%, rgba(40,110,255,0.6) 0%, transparent 40%),
      radial-gradient(ellipse at 95% 80%, rgba(40,110,255,0.6) 0%, transparent 40%),
      linear-gradient(180deg, var(--bg-blue) 0%, var(--bg-blue-deep) 55%, #06208f 100%);
  }
  .page {
    position: absolute; left: 190px; top: 0; width: 820px; height: 1166px;
  }
  .condensed { font-stretch: 75%; font-family: "Open Sans", Arial, sans-serif; }

  /* Header */
  .header { position: absolute; left: 0; top: 0; width: 820px; height: 385px; }
  .sidebar {
    position: absolute; left: 0; top: 0; width: 293px; height: 385px;
    background: var(--panel-light);
  }
  .brand {
    position: absolute; left: 34px; top: 30px;
    display: flex; align-items: center; gap: 9px;
  }
  .brand-mark { width: 46px; height: 46px; border-radius: 50%; background: var(--green); }
  .brand-name {
    font-weight: 800; font-size: 20px; line-height: 1.1; color: #1d2f6b;
    width: 190px;
  }
  .main-nav { position: absolute; left: 40px; top: 120px; list-style: none; }
  .main-nav li {
    font-stretch: 75%; font-weight: 700; font-size: 14.5px; color: var(--ink);
    height: 28.8px; line-height: 22px; text-transform: uppercase;
  }
  .hero {
    position: absolute; left: 293px; top: 0; width: 527px; height: 385px;
    background:
      radial-gradient(ellipse at 30% 10%, #d8dde3 0%, transparent 35%),
      linear-gradient(150deg, #a9b0b8 0%, #e7e9ec 25%, #1f8be8 45%, #2b98f0 70%, #7fb9e8 100%);
  }

  /* Utility bar */
  .utility-bar {
    position: absolute; left: 0; top: 385px; width: 820px; height: 62px;
    background: var(--green);
  }
  .social { position: absolute; left: 24px; top: 18px; display: flex; gap: 6px; }
  .social span { width: 28px; height: 28px; border-radius: 50%; background: var(--white); }
  .search {
    position: absolute; left: 523px; top: 16px; width: 176px; height: 31px;
    background: var(--white); border: 1px solid #c9d4a6; display: flex;
  }
  .search-field { flex: 1; font-size: 13px; color: #555; padding: 7px 10px; }
  .search-button {
    width: 36px; height: 29px; background: var(--green-dark);
    border-left: 1px solid #c9d4a6; display: flex; align-items: center; justify-content: center;
  }
  .account {
    position: absolute; left: 718px; top: 21px; font-size: 12.5px; color: var(--white);
  }

  /* Intro */
  .intro {
    position: absolute; left: 0; top: 447px; width: 820px; height: 373px;
    background: var(--content-bg);
  }
  .intro-title {
    position: absolute; left: 27px; top: 38px;
    font-stretch: 75%; font-weight: 700; font-size: 31px; color: var(--ink);
    text-transform: uppercase; letter-spacing: 0.2px;
  }
  .intro-body {
    position: absolute; left: 25px; top: 90px; width: 440px;
    font-size: 12.3px; line-height: 22px; color: var(--text);
  }
  .benefits { position: absolute; left: 496px; top: 40px; width: 300px; }
  .benefit { height: 108px; }
  .benefit:nth-child(3) { margin-top: -3px; }
  .benefit h3 {
    font-stretch: 75%; font-weight: 700; font-size: 18.5px; color: var(--green);
    text-transform: uppercase; margin-bottom: 6px;
  }
  .benefit p { font-size: 12.3px; line-height: 17px; color: var(--text); }

  /* Callout band */
  .callout { position: absolute; left: 0; top: 820px; width: 820px; height: 265px; }
  .need-to-know {
    position: absolute; left: 0; top: 0; width: 332px; height: 265px; background: var(--green);
  }
  .need-to-know h2 {
    position: absolute; left: 25px; top: 33px;
    font-stretch: 75%; font-weight: 600; font-size: 25px; color: var(--white); text-transform: uppercase;
  }
  .topic-list { position: absolute; left: 28px; top: 78px; list-style: none; }
  .topic-list li { font-size: 13px; color: var(--white); height: 25.7px; }
  .advisor {
    position: absolute; left: 332px; top: 0; width: 213px; height: 265px; background: var(--dark-1);
  }
  .advisor-photo {
    position: absolute; left: 54px; top: 42px; width: 104px; height: 104px; border-radius: 50%;
    border: 2px solid #cfcfcf;
    background: radial-gradient(circle at 50% 40%, #d9dee3 0%, #9aa2ab 60%, #3c4450 100%);
  }
  .quote-button {
    position: absolute; left: 20px; top: 170px; width: 175px; height: 50px;
    border: 1.5px solid var(--white); color: var(--white);
    font-stretch: 75%; font-weight: 600; font-size: 19px; text-transform: uppercase;
    display: flex; align-items: center; justify-content: center;
  }
  .contact-pitch {
    position: absolute; left: 545px; top: 0; width: 275px; height: 265px; background: var(--dark-2);
    border-left: 1px solid #333;
  }
  .contact-pitch h2 {
    position: absolute; left: 209px; left: 409px;
  }
  .pitch-title {
    position: absolute; left: 209px;
  }
  .contact-pitch .headline {
    position: absolute; left: 209px;
  }
  .contact-pitch h3 {
    position: absolute; left: 209px;
  }
  .pitch {
    position: absolute; left: 209px;
  }
  .contact-pitch .title {
    position: absolute; left: 209px;
  }
  .contact-pitch .heading {
    position: absolute; left: 209px; top: 0;
  }
  .contact-pitch .pitch-heading {
    position: absolute; left: 209px;
  }
  .contact-pitch .pitch-copy {
    position: absolute;
  }
  .pitch-heading {
    position: absolute; left: 209px;
  }
  .contact-pitch .pitch-heading, .contact-pitch .pitch-copy { left: 18px; width: 250px; }
  .contact-pitch .pitch-heading {
    top: 56px; font-stretch: 75%; font-weight: 700; font-size: 18.5px; line-height: 24px;
    color: var(--white); text-transform: uppercase;
  }
  .contact-pitch .pitch-copy {
    top: 143px; font-size: 15.5px; line-height: 17.5px; color: var(--white);
  }

  /* Footer */
  .footer {
    position: absolute; left: 0; top: 1085px; width: 820px; height: 81px; background: var(--footer-bg);
    text-align: center; font-size: 12.5px; line-height: 18px; color: #333; padding-top: 27px;
  }
</style>
</head>
<body>
  <div class="backdrop" role="img" aria-label="Background photograph of glowing blue laptops and binary code"></div>

  <div class="page">
    <header class="header">
      <div class="sidebar">
        <div class="brand">
          <span class="brand-mark"></span>
          <span class="brand-name">Brellin Trade Partners</span>
        </div>
        <ul class="main-nav">
          <li>Home</li>
          <li>About Us</li>
          <li>Product Categories</li>
          <li>Sourcing &amp; Procurment</li>
          <li>Request Quote</li>
          <li>Clients</li>
          <li>Contact Us</li>
        </ul>
      </div>
      <div class="hero" role="img" aria-label="Photograph of large blue 3D arrows with the word Outsourcing"></div>
    </header>

    <div class="utility-bar">
      <div class="social"><span></span><span></span><span></span><span></span></div>
      <div class="search">
        <div class="search-field">Search Here...</div>
        <div class="search-button">
          <svg width="16" height="16" viewBox="0 0 16 16"><circle cx="6.5" cy="6.5" r="4.8" fill="none" stroke="#fff" stroke-width="1.8"/><line x1="10" y1="10" x2="14.5" y2="14.5" stroke="#fff" stroke-width="2" stroke-linecap="round"/></svg>
        </div>
      </div>
      <div class="account">Login /&nbsp; Register</div>
    </div>

    <section class="intro">
      <h1 class="intro-title">Brellin Trade Partners</h1>
      <p class="intro-body">Lorem ipsum dolor sit amet, consectetur adipiscing elit. Praesent at tincidunt dolor, nec pulvinar elit. Vivamus imperdiet ipsum lacus, eu suscipit lacus maximus sed. Donec a posuere magna. Fusce finibus, elit nec semper convallis, odio magna feugiat nibh, eget feugiat elit nunc eu erat. Vestibulum ante ipsum primis in faucibus orci luctus et ultrices posuere cubilia Curae; Aliquam ac ipsum in mi luctus bibendum ac vitae nibh. Cras malesuada consequat dui, efficitur ultrices lectus aliquam ut. Nulla congue sollicitudin suscipit. Phasellus luctus fringilla diam convallis elementum. Curabitur quis lobortis est. Proin venenatis luctus efficitur. Nam tempor mattis nibh, id hendrerit felis malesuada ac. Aliquam sit amet urna eu nulla eleifend bibendum sed ut est. Mauris tempus sodales nibh, eget scelerisque sem viverra sed.</p>
      <div class="benefits">
        <div class="benefit">
          <h3>Access Emerging Markets</h3>
          <p>Lorem ipsum dolor sit amet, consectetur adipiscing elit. Praesent at tincidunt dolor, nec pulvinar elit. Vivamus imperdiet ipsum lacus, maximus sed.</p>
        </div>
        <div class="benefit">
          <h3>Realise Value by Sourcing Direct</h3>
          <p>Lorem ipsum dolor sit amet, consectetur adipiscing elit. Praesent at tincidunt dolor, nec pulvinar elit. Vivamus imperdiet ipsum lacus, maximus sed.</p>
        </div>
        <div class="benefit">
          <h3>Manage Quality and Reliability Risks</h3>
          <p>Lorem ipsum dolor sit amet, consectetur adipiscing elit. Praesent at tincidunt dolor, nec pulvinar elit. Vivamus imperdiet ipsum lacus, maximus sed.</p>
        </div>
      </div>
    </section>

    <section class="callout">
      <div class="need-to-know">
        <h2>What Do You Need to Know</h2>
        <ul class="topic-list">
          <li>Contract Sewing in China</li>
          <li>What is the Process?</li>
          <li>What the Minimum Order?</li>
          <li>Contract Outsourcing FAQ</li>
          <li>Outsourcing Case Study</li>
          <li>Custom Industrial Sewing in China</li>
        </ul>
      </div>
      <div class="advisor">
        <div class="advisor-photo" role="img" aria-label="Portrait photograph of a sourcing advisor"></div>
        <div class="quote-button">Request Quote</div>
      </div>
      <div class="contact-pitch">
        <h2 class="pitch-heading">Outsource your sewing needs to trusted contractors in China</h2>
        <p class="pitch-copy">Please contact us for immediate consultation regarding your outsourcing project.</p>
      </div>
    </section>

    <footer class="footer">© Copyright 2015, Brellin Trade Partners, LLC. All rights reserved.</footer>
  </div>
</body>
</html>
```